Gestaltung einer Webseite für Eventfotografie
quirlmoos hat hervorragende Arbeit geleistet. Das Design ist 1A, sowie die weitere Projektabwicklung, völlig problemlos, sehr freundlich, entgegenkommend und kompetent. Ich kann quirlmoos jederzeit mit 5 Sternen als Designer weiterempfehlen! gernold
Zielgruppe
Eventagenturen, Entscheider in Marketing- bzw. Eventabteilungen von mittelständischen oder großen Firmen sowie Bankettabteilungen von Hotels.
Aufgabenstellung
Neuerstellung Webseitenlayout und programmtechnische Umsetzung einer Webseite.
Die Webseite soll "Das Glanzstück"heissen. Die Wörter "Das Glanzstück" wären grafisch dementsprechend auch zu gestalten.
Die Webseite dient als Schaufenster zur Generierung von Anfragen / Aufträgen die Eventfotografie betreffend. Da der erste Eindruck entscheidend ist, stelle ich mir beim Aufruf der Webseite vor, dass prominent 3-5 Fotos erscheinen. Die Animation der Fotos soll so gestaltet sein, als wenn man Papierabzüge auf einen Tisch legt (Mein Haus, Mein Pferd, mein Boot...)
Darüber hinaus sollen weitere weniger auffällige Eventfotos erscheinen.
Es sollen eine Homepage, eine Kontaktseite, eine Fotogalerieseite, eine Referenzseite (mit Kundennamen und Fotos) und evtl. ein Onlinekalender integriert sein, auf dem der Benutzer das Eventdatum anklicken und seine Anfrage platzieren kann. Impressum ist obligatorisch.
Alle Bereiche sollen übersichtlich und klar gestaltet sein, so dass sich der User schnell orientieren kann.
Auf jeder Unterseite soll ein ca. 5DM-Stück grosser auffälliger "Termin-Anfrage"-Button platziert sein.

```html
<!DOCTYPE html>
<html lang="de">
<head>
<meta charset="utf-8">
<title>Das Glanzstück – Kalender</title>
<link href="https://fonts.googleapis.com/css2?family=Oswald:wght@300;400;500&family=Open+Sans:wght@400;600;700&display=swap" rel="stylesheet">
<style>
  :root {
    --page-bg: #262626;
    --stage-dark: #1e2428;
    --stage-mid: #4d5861;
    --stage-light: #6b7780;
    --white: #ffffff;
    --pink: #d0285a;
    --tab-black: #000000;
    --text-grey: #8a8a8a;
    --text-dark: #222222;
    --link-orange: #e8862a;
    --footer-grey: #6c6c6c;
    --photo-top: #c9ccd0;
    --photo-bottom: #5a4a48;
  }
  * { box-sizing: border-box; margin: 0; padding: 0; }
  html, body { width: 1200px; height: 900px; overflow: hidden; }
  body {
    background: var(--page-bg);
    font-family: "Open Sans", Arial, sans-serif;
    position: relative;
  }
  .stage {
    position: absolute;
    left: 55px; top: 90px;
    width: 1090px; height: 666px;
    overflow: hidden;
    background:
      radial-gradient(ellipse 60% 70% at 32% 48%, var(--stage-light) 0%, var(--stage-mid) 35%, var(--stage-dark) 100%);
  }
  .section-tab {
    position: absolute;
    left: 54px; top: 0;
    width: 224px; height: 28px;
    background: var(--tab-black);
    color: var(--white);
    font-family: "Oswald", sans-serif;
    font-weight: 500;
    font-size: 13px;
    letter-spacing: .5px;
    line-height: 28px;
    padding-left: 16px;
  }
  .headline {
    position: absolute;
    right: calc(1090px - 434px);
    top: 98px;
    text-align: right;
    font-family: "Oswald", sans-serif;
    line-height: 1;
  }
  .headline-kicker { color: var(--pink); font-size: 18px; font-weight: 400; display: block; }
  .headline-main { color: var(--white); font-size: 44px; font-weight: 500; display: block; letter-spacing: -.5px; }
  .event-date {
    position: absolute;
    top: 240px;
    font-family: "Oswald", sans-serif;
    font-size: 21px;
    font-weight: 400;
    color: var(--white);
    white-space: nowrap;
  }
  .event-date.is-highlight { color: var(--pink); }
  .brand {
    position: absolute;
    left: 62px; top: 492px;
    display: flex; align-items: center; gap: 16px;
  }
  .brand-dot {
    width: 110px; height: 110px; border-radius: 50%;
    border: 6px solid var(--white);
  }
  .brand-name {
    font-family: "Oswald", sans-serif;
    font-weight: 400;
    color: var(--white);
    font-size: 40px;
    line-height: 1.02;
    text-transform: uppercase;
  }
  .event-card {
    position: absolute;
    left: 492px; top: 0;
    width: 330px; height: 666px;
    background: var(--white);
    padding: 34px 30px 0 28px;
  }
  .card-close {
    position: absolute; right: 14px; top: 6px;
    font-weight: 700; font-size: 17px; color: var(--text-dark);
  }
  .card-photo {
    width: 244px; height: 175px;
    border: 5px solid var(--white);
    box-shadow: 0 2px 8px rgba(0,0,0,.35);
    background: linear-gradient(180deg, var(--photo-top) 0%, #8c8f94 45%, var(--photo-bottom) 100%);
  }
  .card-title {
    margin-top: 36px;
    font-size: 12px; font-weight: 700; color: var(--text-dark);
    letter-spacing: .2px;
  }
  .card-body {
    margin-top: 16px;
    font-size: 12px; line-height: 1.48; color: var(--text-grey);
    width: 262px;
  }
  .card-body p + p { margin-top: 16px; }
  .card-body a { color: var(--text-dark); }
  .card-body .info-label { margin-top: 30px; }
  .card-body .info-link { color: var(--link-orange); font-weight: 700; margin-top: 0; }
  .card-body .info-note { margin-top: 16px; }
  .card-scroll {
    position: absolute; right: 12px; top: 246px;
    width: 14px; height: 52px;
    border: 1px solid #cfcfcf; border-radius: 2px;
  }
  .card-scroll svg { display: block; margin: 5px auto 16px; }
  .card-nav {
    position: absolute; left: 28px; top: 611px;
    display: flex; gap: 16px;
  }
  .card-count {
    position: absolute; right: 30px; top: 612px;
    font-size: 10px; color: var(--text-grey);
  }
  .site-footer {
    position: absolute;
    left: 55px; top: 764px; width: 1090px;
    display: flex; justify-content: space-between; align-items: center;
    font-size: 11px; color: var(--footer-grey);
  }
  .footer-tools { display: flex; gap: 10px; }
  .footer-copy a { color: #8d8d8d; font-weight: 700; text-decoration: underline; }
</style>
</head>
<body>
  <main class="stage">
    <div class="section-tab">KALENDER</div>

    <h1 class="headline">
      <span class="headline-kicker">DIE NÄCHSTEN</span>
      <span class="headline-main">EVENTS</span>
    </h1>

    <span class="event-date" style="left:226px">14/02/2011</span>
    <span class="event-date is-highlight" style="left:347px">21/02/2011</span>
    <span class="event-date is-highlight" style="left:913px">27/02/2011</span>
    <span class="event-date" style="left:1036px">03/03/2011</span>

    <div class="brand">
      <span class="brand-dot"></span>
      <span class="brand-name">Das<br>Glanz-<br>stück</span>
    </div>

    <article class="event-card">
      <span class="card-close">x</span>
      <div class="card-photo" role="img" aria-label="Foto einer Messehalle mit Ausstellungsständen"></div>
      <h2 class="card-title">DIESES IST DAS ZWEITE EVENT</h2>
      <div class="card-body">
        <p>Unser zweites Event an dem wir teilnehmen und wieder tolle Fotos machen werden. Diese werden dann hier sofort wieder auf unserer Seite aktualisiert. Sie finden die Fotos dann <a href="#">hier</a></p>
        <p>Wir machen von jedem Event die besten Fotos - halten die schönsten Momente für Sie fest und bieten Ihnen mit unserer neuen Webseite den besten Service.</p>
        <p class="info-label">Infos zum Event</p>
        <p class="info-link">www.studio-ahornblatt.de</p>
        <p class="info-note">Wie Sie sehen, kann man hier sehr viele Informationen auf dem kleinen Feld</p>
      </div>
      <div class="card-scroll">
        <svg width="8" height="6" viewBox="0 0 8 6"><path d="M1 5 L4 1 L7 5" fill="none" stroke="#999" stroke-width="1.2"/></svg>
        <svg width="8" height="6" viewBox="0 0 8 6"><path d="M1 1 L4 5 L7 1" fill="none" stroke="#999" stroke-width="1.2"/></svg>
      </div>
      <nav class="card-nav">
        <svg width="26" height="12" viewBox="0 0 26 12"><path d="M25 6 H2 M7 1 L2 6 L7 11" fill="none" stroke="#b5b5b5" stroke-width="1.4" stroke-dasharray="3 2"/></svg>
        <svg width="26" height="12" viewBox="0 0 26 12"><path d="M1 6 H24 M19 1 L24 6 L19 11" fill="none" stroke="#b5b5b5" stroke-width="1.4" stroke-dasharray="3 2"/></svg>
      </nav>
      <span class="card-count">2/16</span>
    </article>
  </main>

  <footer class="site-footer">
    <div class="footer-tools">
      <svg width="14" height="14" viewBox="0 0 14 14"><path d="M1 5V1H5 M9 1H13V5 M13 9V13H9 M5 13H1V9" fill="none" stroke="#6c6c6c" stroke-width="1.4"/></svg>
      <svg width="16" height="14" viewBox="0 0 16 14"><path d="M1 5H4L8 1V13L4 9H1Z" fill="#6c6c6c"/><path d="M11 4Q13 7 11 10" fill="none" stroke="#6c6c6c" stroke-width="1.3"/></svg>
    </div>
    <div class="footer-copy">Copyright © 02/2011 www.studio-ahornblatt.de &nbsp;|&nbsp; <a href="#">info@studio-ahornblatt.de</a></div>
  </footer>
</body>
</html>
```